New home maintenance business, on the back of business card i would like dot points of my services provided.
these include,
General household repairs and maintenance
Painting
Verolin/Plaster Repairs
Fencing
Gardening and landscaping
Cleaning and removals
Doors and windows
Hinges and Locks
Fly screen/ screen door Repairs
I like black,silver, red but ill leav it up to you guys as something may be better for business.. , would also it be possible to create a logo for me incorporating the K&T as i want to make up t shirts in future thankyou
i would also like to put Marco Vintelli on the cards aswell please, and on back change painter to proffesional painter and decorator, please
i like alot of the designs sofar, i cant put my finger on wat 1 yet though!! cheers guys
Business
K&T HOME MAINTENANCE SERVICES
Lewis Vintelli 0467205184
kntmaintenance@postvale.com
ABN:57140328619

```html
<!DOCTYPE html>
<html lang="en">
<head>
<meta charset="utf-8">
<title>K&amp;T Home Maintenance Services – Business Cards</title>
<link rel="stylesheet" href="https://fonts.googleapis.com/css2?family=Open+Sans:wght@400;700&display=swap">
<style>
  :root {
    --backdrop: #e9ecee;
    --panel: #f4f6f7;
    --card-blue: #0f5f8e;
    --card-blue-light: #1a79ad;
    --card-white: #fbfcfc;
    --brand-blue: #1b6c9c;
    --ink-grey: #7a7f84;
    --accent-stripe: #2b86b9;
  }
  * { box-sizing: border-box; margin: 0; padding: 0; }
  html, body { width: 1200px; height: 800px; overflow: hidden; }
  body {
    background: var(--backdrop);
    font-family: "Open Sans", Arial, sans-serif;
    position: relative;
  }

  .business-name {
    font-weight: 700;
    white-space: nowrap;
    letter-spacing: 0.02em;
  }

  .logo-panel {
    position: absolute; left: 790px; top: 0;
    width: 410px; height: 206px;
    background: var(--panel);
    display: flex; align-items: center; justify-content: center;
  }
  .logo-panel .business-name { font-size: 20px; color: var(--brand-blue); }

  .card {
    position: absolute;
    top: 300px; width: 540px; height: 300px;
    box-shadow: 0 10px 24px rgba(0,0,0,0.16);
    display: flex; flex-direction: column; align-items: center;
  }

  .card--back {
    left: 40px;
    background: linear-gradient(160deg, var(--card-blue-light) 0%, var(--card-blue) 55%);
    color: #ffffff;
    padding: 120px 36px 0;
  }
  .card--back .business-name { font-size: 17px; color: #ffffff; }

  .service-list {
    list-style: none; text-align: center;
    margin-top: 22px;
    font-size: 12.5px; line-height: 1.4; color: #ffffff;
  }
  .service-list li { display: inline; }
  .service-list li + li::before { content: " · "; }
  .service-list .is-featured { font-weight: 700; }

  .card--front {
    left: 620px;
    background: var(--card-white);
    border-bottom: 6px solid var(--accent-stripe);
    padding-top: 86px;
  }
  .card--front .business-name { font-size: 17px; color: var(--brand-blue); }

  .contact-name {
    margin-top: 70px;
    font-size: 16px; font-weight: 700; letter-spacing: 0.04em;
    color: var(--brand-blue);
  }
  .contact-line {
    margin-top: 8px; font-size: 12px; color: var(--ink-grey);
  }
  .contact-line b { color: var(--brand-blue); font-weight: 700; }
</style>
</head>
<body>

  <section class="logo-panel" aria-label="Business name">
    <p class="business-name">K&amp;T HOME MAINTENANCE SERVICES</p>
  </section>

  <article class="card card--back" aria-label="Business card back">
    <p class="business-name">K&amp;T HOME MAINTENANCE SERVICES</p>
    <ul class="service-list">
      <li>General Household Repairs And Maintenance</li>
      <li>Professional Painter And Decorator</li>
      <li>Verolin / Plaster Repairs</li>
      <li class="is-featured">Fencing</li>
      <li>Gardening And Landscaping</li>
      <li class="is-featured">Cleaning And Removals</li>
      <li>Doors And Windows</li>
      <li>Hinges And Locks</li>
      <li>Fly Screen / Screen Door Repairs</li>
    </ul>
  </article>

  <article class="card card--front" aria-label="Business card front">
    <p class="business-name">K&amp;T HOME MAINTENANCE SERVICES</p>
    <p class="contact-name">LEWIS VINTELLI</p>
    <p class="contact-line"><b>T:</b> 0467205184 &middot; <b>E:</b> kntmaintenance@postvale.com</p>
  </article>

</body>
</html>
```